Stand out flyer needed for Boxing gym

Hi we need a trifold brochure designed for our outdoor boxing business it will be delivered to doctors and nutritionists to help their patients be healthier and get fit.We have supplied high res pictures for you to use in the brochure. We need a design that use a lot of yellow so it captures their attention. You can check our website for design colours www.ridgepunch.com.au

Target Market(s)

Overweight or unfit people looking to change their lives

Industry/Entity Type

Health And Wellness

Font styles to use
Sans Serif

Colors
fbee3d
ffffff
000000

Requirements
Must have
• (main heading - large bold font) Get fit lose weight & feel great
• (bold) Unlimited outdoor boxing classes $14.95
• Complete affordability & No judgements guaranteed
• (bold) Tailored programs (bold)
• Our programs are structured so that members of all fitness levels feel confident & comfortable during their start-up phase allowing you to quickly build your fitness
• (bold) Injury prevention (bold)
• Our training systems include techniques that will help you avoid injuries and build balanced strength
• (bold) Strengthen & Tone your core (bold)
• You're core muscles are some of you're most important muscles. Each workout you do incorporates core exercises to help avoid injuries and make you're total body stronger
• (bold) Wake up with more energy(bold)
• Every class you'll do will have you filled with energy the will pump you up for the rest of your day
• (bold) Sleep better(bold)
• One of the best parts of exercise is the benefit it has on your sleeping patterns. You'll sleep deeper & more sound
• (bold) Supportive environment (bold)
• At RIDGE PUNCH you'll be surrounded by trainers & other members who are there to encourage & motivate you to reach your goals and to get you moving more.
• Coupon code: SunRise27

```html
<!DOCTYPE html>
<html lang="en">
<head>
<meta charset="utf-8">
<title>Ridge Punch – Outdoor Boxing Brochure</title>
<link rel="stylesheet" href="https://fonts.googleapis.com/css2?family=Saira+Condensed:wght@700;800&family=Questrial&display=swap">
<style>
  :root {
    --yellow: #fbee3d;
    --black: #000000;
    --white: #ffffff;
    --ink: #2a2a2a;
    --display: "Saira Condensed", "Arial Narrow", sans-serif;
    --body: "Questrial", "Helvetica", sans-serif;
  }
  html, body { margin: 0; padding: 0; overflow: hidden; background: #e6e6e6; }
  .brochure {
    position: relative; width: 1200px; height: 848px; overflow: hidden;
    background: var(--white); font-family: var(--body); color: var(--ink);
  }
  .backdrop { position: absolute; inset: 0; width: 1200px; height: 848px; }

  /* inside panel */
  .section-title {
    position: absolute; margin: 0; font-family: var(--display); font-weight: 800;
    font-size: 31px; line-height: 1; letter-spacing: 0.2px;
  }
  .section-title--toughness { left: 30px; top: 40px; color: var(--yellow); }
  .section-title--culture { left: 30px; top: 380px; color: var(--black); }
  .section-marker { position: absolute; left: 0; top: 382px; width: 23px; height: 31px; background: var(--black); }
  .copy {
    position: absolute; left: 31px; margin: 0; font-size: 15.8px; line-height: 20.6px; color: var(--ink);
  }
  .copy .line { display: block; width: 337px; white-space: nowrap; text-align: justify; text-align-last: justify; }
  .copy .line--end { text-align-last: left; }
  .copy--toughness { top: 86px; }
  .copy--guarantee { top: 265px; }
  .copy--culture { top: 417px; }
  .copy--coaches { top: 592px; }
  .copy--coaches .w1 { width: 296px; }
  .copy--coaches .w2 { width: 282px; }
  .copy--coaches .w3 { width: 269px; }
  .copy--coaches .w4 { width: 255px; }
  .copy--coaches .w5 { width: 242px; }

  /* middle panel */
  .offer { position: absolute; left: 404px; top: 292px; width: 382px; text-align: center; }
  .offer__lead {
    margin: 0; font-family: var(--display); font-weight: 800; font-size: 84px;
    line-height: 0.9; color: var(--yellow); letter-spacing: 0.5px;
  }
  .offer__classes {
    margin: 6px 0 0; font-family: var(--display); font-weight: 700; font-size: 48px;
    line-height: 0.98; color: var(--white); letter-spacing: 0.5px;
  }
  .offer__price { color: var(--yellow); }
  .offer__promise {
    margin: 10px 0 0; font-family: var(--display); font-weight: 700; font-size: 21px;
    line-height: 1.2; color: var(--white);
  }
  .brand-box {
    position: absolute; box-sizing: border-box; display: flex; align-items: center;
    justify-content: center; border: 2px solid currentColor;
    font-family: var(--display); font-weight: 700; line-height: 1; white-space: nowrap;
  }
  .brand-box--contact { left: 574px; top: 685px; width: 191px; height: 67px; color: var(--white); font-size: 34px; letter-spacing: 1px; }
  .brand-box--cover { left: 849px; top: 37px; width: 288px; height: 101px; color: var(--black); font-size: 52px; letter-spacing: 1.5px; }
  .contact {
    position: absolute; left: 540px; top: 762px; width: 260px; margin: 0; text-align: center;
    font-family: var(--display); font-weight: 700; color: var(--white); font-style: normal;
  }
  .contact__phone { display: block; font-size: 20px; letter-spacing: 1px; line-height: 1.2; }
  .contact__line { display: block; font-size: 15px; line-height: 1.5; }

  /* cover panel */
  .cover-title {
    position: absolute; left: 838px; top: 584px; margin: 0; font-family: var(--display);
    font-weight: 800; color: var(--black); line-height: 0.78;
  }
  .cover-title__big { display: block; font-size: 120px; letter-spacing: -1px; }
  .cover-title__small { display: block; font-size: 40px; line-height: 1; margin-top: 4px; }
</style>
</head>
<body>
<main class="brochure">
  <svg class="backdrop" viewBox="0 0 1300 919" preserveAspectRatio="none">
    <defs>
      <linearGradient id="mist" x1="0" y1="0" x2="0" y2="1">
        <stop offset="0" stop-color="#f4f4f4"/>
        <stop offset="0.6" stop-color="#e9e9e9"/>
        <stop offset="1" stop-color="#f6f6f6"/>
      </linearGradient>
      <radialGradient id="shadowFigure" cx="0.5" cy="0.35" r="0.6">
        <stop offset="0" stop-color="#2a2a2a"/>
        <stop offset="1" stop-color="#000000"/>
      </radialGradient>
      <linearGradient id="citySky" x1="0" y1="0" x2="0" y2="1">
        <stop offset="0" stop-color="#f7f7f7"/>
        <stop offset="0.35" stop-color="#cfcac2"/>
        <stop offset="0.7" stop-color="#8a8883"/>
        <stop offset="1" stop-color="#d8d8d8"/>
      </linearGradient>
    </defs>

    <!-- inside panel -->
    <rect x="0" y="0" width="425" height="919" fill="#ffffff"/>
    <rect x="0" y="88" width="425" height="831" fill="url(#mist)" role="img" aria-label="Faint photo of a boxer training outdoors"/>
    <rect x="0" y="0" width="425" height="88" fill="#000000"/>
    <polygon points="425,600 425,919 220,919" fill="#000000"/>

    <!-- middle panel -->
    <rect x="425" y="0" width="437" height="919" fill="url(#shadowFigure)" role="img" aria-label="Dark faded photo of a boxer"/>
    <polygon points="630,0 862,0 862,310" fill="#fbee3d"/>
    <polygon points="425,600 630,919 425,919" fill="#fbee3d"/>

    <!-- cover panel -->
    <rect x="862" y="0" width="438" height="919" fill="#ffffff"/>
    <rect x="862" y="150" width="438" height="560" fill="url(#citySky)" role="img" aria-label="Hooded boxer in guard stance in front of a city skyline at sunrise"/>
    <polygon points="1300,250 1300,480 1080,585" fill="#000000"/>
    <polygon points="862,680 1300,480 1300,919 862,919" fill="#fbee3d"/>
    <ellipse cx="1205" cy="465" rx="72" ry="58" fill="#ffffff" role="img" aria-label="Boxing glove icon"/>
  </svg>

  <h2 class="section-title section-title--toughness">Find Your Toughness</h2>
  <p class="copy copy--toughness">
    <span class="line">What’s the difference between successful</span>
    <span class="line">people and the rest? Toughness! Not just</span>
    <span class="line">physically but mentally as well. Everyday</span>
    <span class="line">you face pressure, struggles and choices.</span>
    <span class="line">No one can do it for you. You must dig deep</span>
    <span class="line">and find your inner toughness. That primal</span>
    <span class="line">instinct inside you to not just survive but to</span>
    <span class="line line--end">thrive.</span>
  </p>
  <p class="copy copy--guarantee">
    <span class="line">We guarentee Every session you complete</span>
    <span class="line">will have you both mentally and physically</span>
    <span class="line">tougher ready to take on the tough</span>
    <span class="line line--end">challenges &amp; decisions you face everyday.</span>
  </p>

  <span class="section-marker"></span>
  <h2 class="section-title section-title--culture">Ridge Punch Culture</h2>
  <p class="copy copy--culture">
    <span class="line">Some days you just don’t feel like getting</span>
    <span class="line">back up and it’s those days you need to be</span>
    <span class="line">surrounded by people. Not just your</span>
    <span class="line">friends. Not just your family. But People</span>
    <span class="line">who want you to reach your goals as much</span>
    <span class="line">as they want to reach their own. People</span>
    <span class="line">who feel that your success is in turn their</span>
    <span class="line line--end">success.</span>
  </p>
  <p class="copy copy--coaches">
    <span class="line line--end">This is what Ridge Punch is all about.</span>
    <span class="line w1">We employ the best coaches who</span>
    <span class="line w2">have a passion for seeing you</span>
    <span class="line w3">succeed &amp; our members strive to</span>
    <span class="line w4">help their teammates achieve</span>
    <span class="line w5 line--end">everything they set their minds</span>
    <span class="line line--end">on.</span>
  </p>

  <section class="offer">
    <p class="offer__lead">Unlimited</p>
    <p class="offer__classes">Outdoor Boxing<br>Classes <span class="offer__price">$14.95</span></p>
    <p class="offer__promise">Complete Affordability &amp;<br>No Judgements Guaranteed</p>
  </section>

  <div class="brand-box brand-box--contact">RIDGE PUNCH</div>
  <address class="contact">
    <span class="contact__phone">0400123987</span>
    <span class="contact__line">info@ridgepunch.com.au</span>
    <span class="contact__line">www.ridgepunch.com.au</span>
  </address>

  <div class="brand-box brand-box--cover">RIDGE PUNCH</div>
  <h1 class="cover-title">
    <span class="cover-title__big">Get</span>
    <span class="cover-title__big">Fit Lose</span>
    <span class="cover-title__small">Weight &amp; Feel Great</span>
  </h1>
</main>
</body>
</html>
```